Kestowell Chardonnay Wine Label 2024

We need a wine label design for a small, family-owned vineyard in Broke, Hunter Valley of NSW (Australia). The vineyard is called Kestowell and we have an existing logo and 'brand book' for the vineyard home that is rented out for short stay bookings. This is attached and includes font style, colour palette and our Kestowell logo for the accommodation (we're not wedded to this but also probably not after a completely different rethink either as we want the accommodation and the wine to feel part of the same thing.

Project:
The initial label requirement (front and back) is for the Kestowell 2024 Chardonnay, which is called 'Marigold'. The label would need to be able to extend to other varietals (eg Verdehlo and Sparkling) in 2025. Attached is draft copy for front and back for the 2024 Chardonnay as a guide.

STYLE: We like a relatively simple, classic design and have played with both a dark (navy) and a light background (white/cream). Based on the final label design we will order a Tarquo colour to pick up on the label theme.

The Chardonnay bottle dimensions are attached, as is our logo file (if that helps)

Target Market(s)

online 25-50 yearold

Industry/Entity Type

Wine

Requirements
Must have
• front and back label design Kestowell logo and name

```html
<!DOCTYPE html>
<html lang="en">
<head>
<meta charset="UTF-8">
<title>Kestowell Marigold 2024 Chardonnay – Front Label</title>
<link href="https://fonts.googleapis.com/css2?family=Crimson+Text:wght@400&family=Roboto:wght@400;700&display=swap" rel="stylesheet">
<style>
  :root {
    --backdrop: #e4dbcf;
    --label-paper: #f7f7f6;
    --label-shade: #e9e9e8;
    --brand-blue: #2a87c4;
    --brand-blue-deep: #1f6fa8;
    --ink: #231815;
  }
  * { margin: 0; padding: 0; box-sizing: border-box; }
  html, body {
    width: 800px;
    height: 1200px;
    overflow: hidden;
    background: var(--backdrop);
  }
  .canvas {
    position: relative;
    width: 800px;
    height: 1200px;
  }
  .front-label {
    position: absolute;
    left: 80px;
    top: 210px;
    width: 640px;
    height: 780px;
    background: linear-gradient(90deg, var(--label-shade) 0%, var(--label-paper) 18%, var(--label-paper) 82%, var(--label-shade) 100%);
    overflow: hidden;
  }
  .brand-dot {
    position: absolute;
    right: 40px;
    top: 70px;
    width: 70px;
    height: 70px;
    border-radius: 50%;
    background: var(--brand-blue);
  }
  .brand-name {
    position: absolute;
    left: 0;
    right: 0;
    top: 210px;
    text-align: center;
    font-family: "Crimson Text", serif;
    font-weight: 400;
    font-size: 132px;
    line-height: 1;
    color: var(--brand-blue);
    letter-spacing: 1px;
  }
  .wine-details {
    position: absolute;
    left: 0;
    right: 0;
    top: 525px;
    text-align: center;
    font-family: "Roboto", sans-serif;
    color: var(--ink);
  }
  .wine-name {
    font-weight: 700;
    font-size: 46px;
    line-height: 56px;
  }
  .wine-vintage {
    font-weight: 400;
    font-size: 46px;
    line-height: 56px;
  }
  .rule {
    width: 390px;
    height: 3px;
    margin: 14px auto 10px;
    background: var(--brand-blue);
  }
  .region {
    font-weight: 400;
    font-size: 35px;
    line-height: 42px;
    color: var(--brand-blue);
  }
  .volume {
    position: absolute;
    right: 14px;
    bottom: 82px;
    font-family: "Roboto", sans-serif;
    font-weight: 700;
    font-size: 22px;
    color: var(--ink);
  }
</style>
</head>
<body>
  <main class="canvas">
    <section class="front-label">
      <span class="brand-dot" aria-hidden="true"></span>
      <h1 class="brand-name">Kestowell</h1>
      <div class="wine-details">
        <p class="wine-name">Marigold</p>
        <p class="wine-vintage">2024 Chardonnay</p>
        <div class="rule"></div>
        <p class="region">Hunter Valley</p>
      </div>
      <p class="volume">750ml</p>
    </section>
  </main>
</body>
</html>
```